Labeling for Organic Food

we need a label design for

1. Organic Red Rice
2. Organic wild honey

it is going to be the same design in different dimensions.

1. Organic Red Rice
Dimension 1 28*18.5cm
Dimension 2 13.5*8cm

2. Organic Honey
12*6cm
Updates

There is an update in the brief about using the Bhutanese color scheme. Please check it out.

Target Market(s)

people with the concern of health and the environment.

Requirements
Must have
• 1. our logo
• 2. All the info
• 3. A natural feel
• 4. I would prefer minimalistic style
• 5. Please include Bhutanese national colours as attached.

```html
<!DOCTYPE html>
<html lang="en">
<head>
<meta charset="utf-8">
<title>Terraleaf Organic Red Rice Label</title>
<link rel="stylesheet" href="https://fonts.googleapis.com/css2?family=Fira+Sans+Condensed:wght@500;600;700;800&display=swap">
<style>
  :root {
    --page: #ffffff;
    --kraft-light: #e9d6b6;
    --kraft: #d9bf98;
    --kraft-deep: #c4a47c;
    --mountain: #b89a78;
    --ink: #231f1d;
    --leaf: #9bd04f;
    --band: #b7e36a;
    --band-edge: #8fc343;
    --rice-dark: #6e2a17;
    --rice: #a54a2a;
    --rice-light: #d17a52;
    --tag: #ffffff;
    --small-text: #f4e8e0;
  }
  * { margin: 0; padding: 0; box-sizing: border-box; }
  html, body {
    width: 1200px; height: 1200px; overflow: hidden;
    background: var(--page);
    font-family: "Fira Sans Condensed", sans-serif;
    color: var(--ink);
  }
  .label {
    position: absolute; left: 250px; top: 80px;
    width: 700px; height: 1040px;
    border-radius: 34px 34px 10px 10px;
    overflow: hidden;
    background: var(--kraft);
  }
  .landscape {
    position: absolute; inset: 0 0 auto 0; height: 560px;
    background: linear-gradient(180deg, var(--kraft-light) 0%, var(--mountain) 45%, var(--kraft) 100%);
  }
  .hang-hole {
    position: absolute; left: 282px; top: 44px;
    width: 136px; height: 32px; border-radius: 16px;
    background: var(--page);
  }
  .brand {
    position: absolute; left: 0; right: 0; top: 285px;
    display: flex; align-items: center; justify-content: center; gap: 18px;
  }
  .brand-dot {
    width: 34px; height: 34px; border-radius: 50%;
    background: var(--leaf);
  }
  .brand-name {
    font-weight: 800; font-size: 128px; line-height: 1;
    color: var(--ink); letter-spacing: -1px;
  }
  .info {
    position: absolute; left: 0; right: 0; top: 540px; height: 190px;
    background: linear-gradient(180deg, var(--kraft) 0%, var(--kraft-light) 100%);
    text-align: center; padding: 26px 44px 0;
  }
  .product-title {
    font-weight: 700; font-size: 40px; line-height: 1.1; margin-bottom: 10px;
  }
  .product-desc {
    font-weight: 600; font-size: 21px; line-height: 1.3;
  }
  .name-band {
    position: absolute; left: 0; right: 0; top: 730px; height: 92px;
    background: var(--band);
    border-bottom: 4px solid var(--band-edge);
    display: flex; align-items: center; justify-content: center;
  }
  .name-band h2 {
    font-weight: 800; font-size: 62px; letter-spacing: 1px; line-height: 1;
  }
  .rice-photo {
    position: absolute; left: 0; right: 0; top: 822px; bottom: 0;
    background: radial-gradient(ellipse at 40% 40%, var(--rice-light) 0%, var(--rice) 45%, var(--rice-dark) 100%);
  }
  .storage {
    position: absolute; left: 24px; top: 862px;
    font-weight: 700; font-size: 15px; line-height: 1.35;
    color: var(--small-text); text-align: right; width: 210px;
  }
  .weight-tag {
    position: absolute; left: 255px; top: 960px;
    width: 170px; height: 56px; border-radius: 8px;
    background: var(--tag);
    display: flex; align-items: center; justify-content: center;
    font-weight: 800; font-size: 40px;
  }
  .distributor {
    position: absolute; left: 448px; top: 900px; width: 240px;
    font-weight: 700; font-size: 14px; line-height: 1.4;
    color: var(--small-text);
  }
</style>
</head>
<body>
  <main class="label">
    <div class="landscape" role="img" aria-label="Soft illustration of Himalayan mountain ridges in kraft tones"></div>
    <div class="hang-hole"></div>

    <div class="brand">
      <span class="brand-name">Terraleaf</span>
      <span class="brand-dot"></span>
    </div>

    <section class="info">
      <h1 class="product-title">Organic Bhutanese Red Rice</h1>
      <p class="product-desc">This organic red rice is 100% sourced from families farming around the remote unpolluted lands in the Himalayans in Bhutan. Chemical preservatives free, Gluten free, Mineral rich, Organic Red Rice is the healthiest choice for you and your loved ones.</p>
    </section>

    <div class="name-band"><h2>ORGANIC RED RICE</h2></div>

    <div class="rice-photo" role="img" aria-label="Close-up photograph of red rice grains"></div>

    <p class="storage">Store in a cool and dry place<br>Best before 31/12/19</p>
    <div class="weight-tag">500gm</div>
    <p class="distributor">Product of Bhutan Distributed by<br>Terraleaf 24 Meadow Row<br>Singapore 600024</p>
  </main>
</body>
</html>
```